Rancho Brisolo Wine Bottle Label

Hello! We are looking for a wine bottle label design for our private, family winery located in Chico, CA. The name of our home/ranch/vineyard is Rancho Brisolo ('the exit'), which is inspired by our hilltop location, panoramic views of the valley, and sensation of escaping from the busy world below.

We planted our vineyard in 2011 and are now bottling our first harvest from fall of 2013. We planted all Italian varietals on our land: syrah, primitivo, and montepulciano. The wine we make is the culmination of all the love, support and effort poured into the process by our family and friends.

The task at hand: we are looking for a clean, simple front and back wine label design.

Front Label Content:
RB and/or Rancho Brisolo
Estate Grown
Chico, CA
Varietal (use Syrah for placeholder)
Year (use 2013 for placeholder)

Back Label Content:
Running list of names of all family and friends who have participated in the process (use a text fill for placeholder)

Aesthetic Description:
Simple, clean, contemporary, text based design (see attached logo idea, Image #1)
Like the brown paper with stamped lettering look & feel
Like the classic clear label with gold lettering look & feel
Option to incorporated a simple background image/sketch of the view overlooking the valley (see attached Image #2 and #3)
Additional inspirational images attached for reference (Images #3- )

General Size Requirement:
Front Label - 4"tall by 3 1/2" wide
Back Label - 4"tall by 3 1/2" wide

Format:
Please submit Photoshop or Illustrator or InDesign Files and PDF/EPS Files.

Industry/Entity Type

Ranch

```html
<!DOCTYPE html>
<html lang="en">
<head>
<meta charset="utf-8">
<title>Rancho Brisolo 2013 Syrah Label</title>
<link rel="stylesheet" href="https://fonts.googleapis.com/css2?family=Chakra+Petch:wght@700&family=Questrial&display=swap">
<style>
  :root {
    --copper-dark: #9a4722;
    --copper-deep: #6c2e17;
    --copper-light: #f9d9c6;
    --cream: #f3e4d9;
    --ink: #0d0a08;
    --ink-soft: #1c1410;
  }
  html, body {
    margin: 0;
    padding: 0;
    width: 1200px;
    height: 1050px;
    overflow: hidden;
  }
  .label {
    position: relative;
    width: 1200px;
    height: 1050px;
    background: linear-gradient(58deg,
      var(--copper-dark) 0%,
      #a95a33 18%,
      var(--copper-light) 42%,
      #f6d3bf 50%,
      #a8603b 62%,
      var(--copper-deep) 72%,
      #8a4d33 80%,
      var(--cream) 96%);
  }
  .label__frame {
    position: absolute;
    left: 0;
    top: 0;
  }
  .label__name {
    position: absolute;
    left: 357px;
    top: 345px;
    width: 500px;
    margin: 0;
    text-align: center;
    font-family: "Questrial", sans-serif;
    font-size: 64px;
    line-height: 1.15;
    color: var(--ink-soft);
  }
  .label__vintage,
  .label__varietal {
    position: absolute;
    margin: 0;
    font-family: "Chakra Petch", sans-serif;
    font-weight: 700;
    color: var(--ink);
    line-height: 1;
    white-space: nowrap;
  }
  .label__vintage {
    left: 538px;
    top: 608px;
    font-size: 60px;
    letter-spacing: 5px;
  }
  .label__varietal {
    left: 510px;
    top: 678px;
    font-size: 60px;
    letter-spacing: 3px;
  }
  .label__estate {
    position: absolute;
    left: 0;
    top: 829px;
    width: 1206px;
    margin: 0;
    text-align: center;
    font-family: "Questrial", sans-serif;
    font-size: 29px;
    color: var(--ink-soft);
    line-height: 1;
  }
</style>
</head>
<body>
  <main class="label">
    <svg class="label__frame" width="1200" height="1050" viewBox="0 0 1200 1050" aria-hidden="true">
      <rect x="345" y="213" width="516" height="578" fill="none" stroke="var(--ink)" stroke-width="5"/>
      <rect x="357" y="225" width="492" height="554" fill="none" stroke="var(--ink)" stroke-width="5"/>
    </svg>
    <p class="label__name">Rancho<br>Brisolo</p>
    <p class="label__vintage">2013</p>
    <h1 class="label__varietal">SYRAH</h1>
    <p class="label__estate">Rancho Brisolo Estate Grown · Chico</p>
  </main>
</body>
</html>
```